One-Page Flat Design for SEO Company [2 DAYS]

We need a one-page flat design for our SEO company. Our current website is http://www.rankorchard.com/. We are looking to completely re-design the site using new flat design techniques.
Below are some examples of the type of style we're going after:
http://pelmora.com/
http://tobyharlan.co.uk/
https://quillet.co/
http://marcusfenley.me/
As you can see- flat, clean, minimal. It is very important you follow this type of style.
For colour scheme, you may use one of the pre-made colour palettes from here:
http://www.wavecrestlab.com/blog/inspiration/24-flat-designs-with-compelling-color-palettes
I've attached a wireframe to be followed.
Hi,

```html
<!DOCTYPE html>
<html lang="en">
<head>
<meta charset="utf-8">
<title>RankOrchard – SEO services that actually work</title>
<link rel="stylesheet" href="https://fonts.googleapis.com/css2?family=Montserrat:wght@400;600;700&family=Titillium+Web:wght@300;400;600;700&display=swap">
<style>
:root{
  --navy:#33506b;
  --navy-deep:#2e4a64;
  --sky:#7fb9c0;
  --sky-card:#7cb6bd;
  --orange:#ff8b4c;
  --mint:#40c4a5;
  --coral:#ff6a55;
  --white:#ffffff;
  --soft:rgba(255,255,255,.82);
  --line:rgba(255,255,255,.45);
}
*{box-sizing:border-box;margin:0;padding:0}
html,body{width:1200px;height:3290px;overflow:hidden}
body{font-family:"Titillium Web",sans-serif;color:var(--white);background:var(--navy)}
section,header,footer{position:absolute;left:0;width:1200px}

/* header */
.site-header{top:0;height:65px;background:var(--navy-deep)}
.brand{position:absolute;left:205px;top:14px;font:600 26px/36px "Montserrat",sans-serif;letter-spacing:3px}
.nav{position:absolute;left:452px;top:22px;display:flex;list-style:none;font:400 13px/20px "Montserrat",sans-serif;letter-spacing:1px}
.nav li{margin-right:38px}
.nav li:last-child{margin-right:0}

/* hero */
.hero{top:65px;height:327px;background:var(--sky)}
.hero-title{position:absolute;left:205px;top:32px;font:400 50px/58px "Montserrat",sans-serif}
.hero-title strong{font-weight:700}
.hero-lead{position:absolute;left:205px;top:155px;width:620px;font:400 20px/25px "Montserrat",sans-serif}
.btn-outline{position:absolute;left:205px;top:234px;width:154px;height:43px;border:2px solid var(--white);font:400 17px/39px "Montserrat",sans-serif;text-align:center}

/* shared section heading */
.section-title{position:absolute;left:0;width:1200px;text-align:center;font-weight:300;font-size:36px;letter-spacing:2px}
.section-title strong{font-weight:700}
.section-sub{position:absolute;left:0;width:1200px;text-align:center;font-size:15px;line-height:20px;color:var(--soft)}

/* features (why choose / services) */
.features{background:var(--navy)}
.why{top:392px;height:564px}
.services{top:1748px;height:564px;background:var(--mint)}
.feature-list{position:absolute;left:0;width:1200px;height:300px}
.feature{position:absolute;width:220px;margin-left:-110px;text-align:center}
.feature-icon{display:block;margin:0 auto}
.feature-name{font-weight:700;font-size:18px;letter-spacing:1px}
.feature-text{font-size:13px;line-height:19px;color:var(--soft);margin-top:12px}
.arrow{position:absolute}

/* pricing */
.pricing{top:956px;height:661px;background:var(--orange)}
.plans{position:absolute;left:214px;top:179px;width:775px;height:397px;display:flex;gap:4px;align-items:flex-start}
.plan{position:relative;flex:1;height:386px;margin-top:8px;background:var(--sky-card);text-align:center}
.plan-head{height:101px;border-bottom:1px solid var(--line);padding-top:26px}
.plan-name{font-weight:700;font-size:19px;letter-spacing:1px}
.plan-price{font-size:14px;color:var(--soft);margin-top:2px}
.plan-features{list-style:none;font-size:14px;line-height:31px;padding-top:30px}
.plan-cta{position:absolute;left:50%;bottom:26px;width:118px;margin-left:-59px;height:31px;border:1.5px solid var(--white);font-size:13px;line-height:28px;letter-spacing:.5px}
.plan-featured{height:405px;margin-top:0;background:var(--navy)}
.plan-featured .plan-head{height:109px}
.plan-featured .plan-price{color:var(--white)}
.plan-featured .plan-features{padding-top:34px}
.plan-featured .plan-cta{background:var(--white);color:var(--navy);bottom:30px}

/* call to action band */
.cta-band{top:1617px;height:131px;background:var(--navy)}
.cta-text{position:absolute;left:236px;top:50px;font-size:24px;line-height:30px}
.cta-button{position:absolute;left:827px;top:46px;width:129px;height:44px;background:var(--mint);font-weight:700;font-size:14px;line-height:44px;text-align:center;letter-spacing:1px}

/* contact */
.contact{top:2312px;height:620px;background:var(--coral)}
.contact-address{position:absolute;left:0;width:1200px;top:98px;text-align:center;font-size:15px;color:var(--soft)}
.field{position:absolute;background:var(--white);color:#7b7b7b;font-size:14px;padding:12px 20px}
.field-name{left:247px;top:165px;width:339px;height:46px}
.field-email{left:614px;top:165px;width:340px;height:46px}
.field-message{left:247px;top:236px;width:707px;height:159px}
.send{position:absolute;left:534px;top:447px;width:132px;height:47px;background:var(--white);color:var(--coral);font-weight:600;font-size:18px;line-height:47px;text-align:center;letter-spacing:3px}
.social{position:absolute;left:0;width:1200px;top:541px;display:flex;justify-content:center;gap:44px;list-style:none;font-weight:600;font-size:19px}

/* footer */
.site-footer{top:2932px;height:358px;background:var(--navy)}
.footer-brand{position:absolute;left:0;width:1200px;top:82px;text-align:center;font:600 32px/40px "Montserrat",sans-serif;letter-spacing:4px}
.footer-text{position:absolute;left:0;width:1200px;top:162px;text-align:center;font-size:15px;line-height:22px;color:var(--soft)}
.footer-dots{position:absolute;left:0;top:248px}
</style>
</head>
<body>

<header class="site-header">
  <div class="brand">LOGO</div>
  <ul class="nav">
    <li>HOME</li><li>ABOUT</li><li>WORK</li><li>SERVICES</li><li>TEAM</li><li>CONTACT</li>
  </ul>
</header>

<section class="hero">
  <h1 class="hero-title">Finally, <strong>SEO services</strong><br>that actually work.</h1>
  <p class="hero-lead">Top-notch SEO services that are guaranteed to boost your search engine rankings. 100% Searchnest-friendly.</p>
  <div class="btn-outline">Learn More</div>
</section>

<section class="features why">
  <h2 class="section-title" style="top:40px">WHY CHOOSE <strong>RANKORCHARD</strong></h2>
  <p class="section-sub" style="top:98px">Fusce dapibus, tellus ac cursus commodo, tortor mauris condimentum.<br>Duis mollis, est non commodo luctus, nisi erat porttitor ligula, eget lacinia odio sem nec elit.</p>
  <svg class="arrow" style="left:112px;top:236px" width="30" height="90" viewBox="0 0 30 90" fill="none" stroke="#fff" stroke-width="2"><path d="M28 2 L2 45 L28 88"/></svg>
  <svg class="arrow" style="left:1056px;top:236px" width="30" height="90" viewBox="0 0 30 90" fill="none" stroke="#fff" stroke-width="2"><path d="M2 2 L28 45 L2 88"/></svg>
  <div class="feature-list" style="top:232px">
    <div class="feature" style="left:356px">
      <svg class="feature-icon" width="80" height="84" viewBox="0 0 80 84" fill="none" stroke="#fff" stroke-width="3" stroke-linejoin="round"><path d="M22 6 H58 V76 L40 60 L22 76 Z"/><path d="M30 22 H50 M30 30 H50"/></svg>
      <div class="feature-name" style="margin-top:79px">BRANDING</div>
      <p class="feature-text">Lorem ipsum dolor sit amet,<br>consectetuer adipiscing elit,<br>sed diam nonummy nibh.</p>
    </div>
    <div class="feature" style="left:600px">
      <svg class="feature-icon" width="84" height="84" viewBox="0 0 84 84" fill="none" stroke="#fff" stroke-width="3" stroke-linejoin="round"><path d="M16 70 L20 56 L60 16 L70 26 L30 66 Z"/><path d="M54 22 L64 32 M20 56 L30 66"/></svg>
      <div class="feature-name" style="margin-top:79px">DESIGN</div>
      <p class="feature-text">Sed ut perspiciatis unde<br>omnis iste natus error sit<br>voluptatem</p>
    </div>
    <div class="feature" style="left:844px">
      <svg class="feature-icon" width="84" height="84" viewBox="0 0 84 84" fill="none" stroke="#fff" stroke-width="3" stroke-linejoin="round"><rect x="10" y="14" width="64" height="44"/><path d="M42 58 V70 M30 72 H54"/></svg>
      <div class="feature-name" style="margin-top:79px">DEVELOPMENT</div>
      <p class="feature-text">At vero eos et accusamus et<br>iusto odio dignissimos qui<br>blanditiis praesentium</p>
    </div>
  </div>
</section>

<section class="pricing">
  <h2 class="section-title" style="top:40px">SELECT A <strong>BOOSTER PLAN</strong></h2>
  <p class="section-sub" style="top:97px">Neque porro quisquam est, qui dolorem ipsum quia dolor sit amet</p>
  <div class="plans">
    <div class="plan">
      <div class="plan-head"><div class="plan-name">PERSONAL</div><div class="plan-price">$5/Month</div></div>
      <ul class="plan-features"><li>Free feature one</li><li>Unlimited feature two</li><li>Unlimited feature three</li><li>2x feature four</li><li>100x feature five</li></ul>
      <div class="plan-cta">GET STARTED</div>
    </div>
    <div class="plan">
      <div class="plan-head"><div class="plan-name">PROFESSIONAL</div><div class="plan-price">$16/Month</div></div>
      <ul class="plan-features"><li>Free feature one</li><li>Unlimited feature two</li><li>Unlimited feature three</li><li>2x feature four</li><li>100x feature five</li></ul>
      <div class="plan-cta">GET STARTED</div>
    </div>
    <div class="plan plan-featured">
      <div class="plan-head"><div class="plan-name">BUSINESS</div><div class="plan-price">$24/Month</div></div>
      <ul class="plan-features"><li>Free feature one</li><li>Unlimited feature two</li><li>Unlimited feature three</li><li>2x feature four</li><li>100x feature five</li></ul>
      <div class="plan-cta">GET STARTED</div>
    </div>
    <div class="plan">
      <div class="plan-head"><div class="plan-name">ENTERPRISE</div><div class="plan-price">$40/Month</div></div>
      <ul class="plan-features"><li>Free feature one</li><li>Unlimited feature two</li><li>Unlimited feature three</li><li>2x feature four</li><li>100x feature five</li></ul>
      <div class="plan-cta">GET STARTED</div>
    </div>
  </div>
</section>

<section class="cta-band">
  <p class="cta-text">Duis mollis est non commodo luctus nisi erat porttitor.</p>
  <div class="cta-button">BUTTON</div>
</section>

<section class="features services">
  <h2 class="section-title" style="top:46px">INDIVIDUAL <strong>SEO SERVICES</strong></h2>
  <p class="section-sub" style="top:102px">Fusce dapibus, tellus ac cursus commodo, tortor mauris condimentum.<br>Duis mollis, est non commodo luctus, nisi erat porttitor ligula, eget lacinia odio sem nec elit.</p>
  <svg class="arrow" style="left:112px;top:238px" width="30" height="90" viewBox="0 0 30 90" fill="none" stroke="#fff" stroke-width="2"><path d="M28 2 L2 45 L28 88"/></svg>
  <svg class="arrow" style="left:1056px;top:238px" width="30" height="90" viewBox="0 0 30 90" fill="none" stroke="#fff" stroke-width="2"><path d="M2 2 L28 45 L2 88"/></svg>
  <div class="feature-list" style="top:199px">
    <div class="feature" style="left:356px">
      <svg class="feature-icon" width="150" height="150" viewBox="0 0 150 150" fill="none" stroke="#fff" stroke-width="3" stroke-linejoin="round"><circle cx="75" cy="75" r="73"/><path d="M46 60 H62 L88 90 H104 M46 90 H62 L70 81 M80 69 L88 60 H104 M96 52 L104 60 L96 68 M96 82 L104 90 L96 98"/></svg>
      <div class="feature-name" style="margin-top:46px">BRANDING</div>
      <p class="feature-text" style="margin-top:8px">Lorem ipsum dolor sit amet,<br>consectetuer adipiscing elit,<br>sed diam nonummy nibh.</p>
    </div>
    <div class="feature" style="left:600px">
      <svg class="feature-icon" width="150" height="150" viewBox="0 0 150 150" fill="none" stroke="#fff" stroke-width="3" stroke-linejoin="round"><circle cx="75" cy="75" r="73"/><path d="M50 76 V62 H100 M92 54 L100 62 L92 70 M100 74 V88 H50 M58 80 L50 88 L58 96"/></svg>
      <div class="feature-name" style="margin-top:46px">DESIGN</div>
      <p class="feature-text" style="margin-top:8px">Sed ut perspiciatis unde<br>omnis iste natus error sit<br>voluptatem</p>
    </div>
    <div class="feature" style="left:844px">
      <svg class="feature-icon" width="150" height="150" viewBox="0 0 150 150" fill="none" stroke="#fff" stroke-width="3" stroke-linejoin="round"><circle cx="75" cy="75" r="73"/><path d="M50 56 L88 46 L92 56"/><rect x="50" y="56" width="50" height="40"/><path d="M100 68 H84 V82 H100"/><circle cx="90" cy="75" r="2"/></svg>
      <div class="feature-name" style="margin-top:46px">DEVELOPMENT</div>
      <p class="feature-text" style="margin-top:8px">At vero eos et accusamus et<br>iusto odio dignissimos qui<br>blanditiis praesentium.</p>
    </div>
  </div>
</section>

<section class="contact">
  <h2 class="section-title" style="top:40px">GET IN <strong>TOUCH</strong></h2>
  <p class="contact-address">48 Larkfield Row, Brookhaven, OR 97301, United States of America. Tel: (503) 555-0142</p>
  <div class="field field-name">Your Name</div>
  <div class="field field-email">Your Email</div>
  <div class="field field-message">Your Message</div>
  <div class="send">SEND</div>
  <ul class="social"><li>Friendloop</li><li>Chirpwire</li><li>Searchnest</li><li>Workchain</li></ul>
</section>

<footer class="site-footer">
  <div class="footer-brand">LOGO</div>
  <p class="footer-text">Fusce dapibus, tellus ac cursus commodo, tortor mauris condimentum.<br>Duis mollis, est non commodo luctus, nisi erat porttitor ligula.</p>
  <svg class="footer-dots" width="1200" height="50" viewBox="0 0 1200 50" fill="none" stroke="#fff" stroke-width="1.5"><circle cx="528" cy="23" r="21"/><circle cx="600" cy="23" r="21"/><circle cx="672" cy="23" r="21"/></svg>
</footer>

</body>
</html>
```